Redesign for a start up airline technology. The website is trelunor.com.

I need a PowerPoint template that complements our website. I can provide our current template as a starting point.

```html
<!DOCTYPE html>
<html lang="en">
<head>
<meta charset="utf-8">
<title>Trelunor – Presentation Template</title>
<link rel="stylesheet" href="https://fonts.googleapis.com/css2?family=Rubik:wght@700;800&family=Karla:wght@400;700&family=Lato:wght@400;700&display=swap">
<style>
:root{
  --bg:#e4e4e4;
  --white:#ffffff;
  --blue:#0b6db6;
  --navy:#0c3f8c;
  --title-blue:#1677c2;
  --cyan:#12a7e3;
  --gold:#c7a250;
  --ink:#2a2f38;
  --dark1:#16284a;
  --dark2:#1f4d7c;
  --band:#335d8c;
  --faint:#c9ced6;
}
*{margin:0;padding:0;box-sizing:border-box}
html,body{width:1200px;height:1200px;overflow:hidden;background:radial-gradient(circle at 50% 50%,#d7d7d7 0%,#ececec 70%,#f1f1f1 100%);font-family:"Karla",sans-serif;color:var(--ink)}
.slide{position:absolute;width:360px;height:270px;background:var(--white);overflow:hidden;box-shadow:0 2px 6px rgba(0,0,0,.18)}
.s1{left:216px;top:153px}.s2{left:624px;top:153px}
.s3{left:216px;top:489px}.s4{left:624px;top:489px}
.s5{left:216px;top:825px}.s6{left:624px;top:825px}
.abs{position:absolute}
.confidential{position:absolute;font-family:"Karla",sans-serif;font-size:3px;letter-spacing:.3px;text-transform:uppercase;color:#c5d3e6}
.confidential.light{color:#b8bcc4}
.photo{position:absolute}
.slide-title{position:absolute;font-family:"Rubik",sans-serif;font-weight:800;font-size:15.5px;color:var(--navy);white-space:nowrap}
.body{font-size:5.3px;line-height:9.6px;color:#333}
.footer-band{position:absolute;left:0;bottom:0;width:360px;height:25px;background:var(--blue)}

/* cover */
.s1{background:linear-gradient(180deg,var(--dark1) 0%,var(--dark2) 60%,#22679a 100%)}
.s1 .band{position:absolute;left:0;top:84px;width:360px;height:102px;background:var(--band)}
.s1 .brand{position:absolute;left:131px;top:117px;font-family:"Rubik",sans-serif;font-weight:800;font-size:24px;color:#7fc4ea;display:flex;align-items:center;gap:6px}
.s1 .brand i{display:inline-block;width:9px;height:9px;border-radius:50%;background:#7fc4ea}

/* who we are */
.s2 .block{position:absolute;left:0;top:0;width:91px;height:132px;background:var(--blue)}
.s2 .text{position:absolute;left:198px;top:83px;width:146px}
.s2 .text p{margin-bottom:5px;font-size:5.3px;line-height:9.6px}

/* team */
.s3 .lower{position:absolute;left:0;top:174px;width:360px;height:96px;background:var(--blue)}
.s3 .slide-title{left:0;width:360px;text-align:center;top:31px;color:var(--title-blue)}
.member{position:absolute;top:88px;width:86px;text-align:center;font-family:"Lato",sans-serif;color:#fff;font-size:6.6px;line-height:10.5px}
.member .portrait{width:86px;height:126px;margin-bottom:8px}
.member .name{font-weight:700}

/* what we do */
.s4 .side{position:absolute;left:276px;top:0;width:84px;height:270px;background:var(--blue)}
.s4 .slide-title{left:27px;top:26px;color:var(--title-blue)}
.s4 .lead{position:absolute;left:27px;top:57px;font-family:"Karla",sans-serif;font-weight:700;font-size:5.6px;color:#111}
.s4 .body{position:absolute;left:27px;top:78px;width:145px;font-size:5.1px;line-height:9.8px}
.s4 ul{position:absolute;left:27px;top:143px;width:120px;list-style:none}
.s4 li{position:relative;padding-left:12px;font-size:4.8px;line-height:8.6px;margin-bottom:4.5px}
.s4 li::before{content:"";position:absolute;left:1px;top:1.5px;width:4px;height:4px;border:1.2px solid var(--cyan);border-radius:50%}

/* who we serve */
.s5 .slide-title{left:42px;top:40px}
.client{position:absolute;width:110px}
.client .badge{position:absolute;left:-28px;top:0;width:19px;height:19px;border-radius:50% 0 50% 50%;color:#fff;font-size:6px;display:flex;align-items:center;justify-content:center;font-family:"Lato",sans-serif}
.client .badge.navy{background:var(--navy)}
.client .badge.cyan{background:var(--cyan)}
.client h3{font-family:"Lato",sans-serif;font-weight:400;font-size:5.4px;color:var(--cyan);margin-bottom:3px}
.client h3.dark{color:var(--navy)}
.client p{font-family:"Lato",sans-serif;font-size:5px;line-height:8.4px;color:#222}

/* process */
.step{position:absolute;top:122px;width:60px}
.step .num{font-family:"Rubik",sans-serif;font-weight:400;font-size:18px;line-height:20px;color:var(--blue)}
.step .num.light{color:#7cc7ee}
.step .line{position:absolute;left:34px;top:10px;width:34px;height:1px;background:#cfd4da}
.step .line::after{content:"";position:absolute;right:-1px;top:-1px;width:3px;height:3px;border-radius:50%;background:#cfd4da}
.step h4{font-weight:400;font-size:5px;color:var(--gold);margin:4px 0 12px}
.step p{font-size:4.3px;line-height:6px;color:#333;width:54px}
</style>
</head>
<body>

<section class="slide s1">
  <div class="band"></div>
  <div class="abs" role="img" aria-label="Faint line drawing of aircraft landing gear" style="left:51px;top:84px;width:56px;height:88px;background:linear-gradient(180deg,rgba(200,215,235,.25),rgba(200,215,235,.12))"></div>
  <div class="brand"><i></i>Trelunor</div>
  <div class="confidential" style="right:15px;top:13px">Confidential and proprietary</div>
</section>

<section class="slide s2">
  <div class="block"></div>
  <div class="abs" role="img" aria-label="Faint technical drawing of landing gear" style="right:0;top:0;width:100px;height:150px;background:linear-gradient(180deg,rgba(180,186,196,.28),rgba(180,186,196,.05))"></div>
  <div class="photo" role="img" aria-label="Photo of an aircraft nose landing gear wheel on the tarmac" style="left:27px;top:33px;width:145px;height:217px;background:linear-gradient(180deg,#5d6166 0%,#a9adb3 35%,#8e9196 65%,#6a6a66 100%)"></div>
  <h2 class="slide-title" style="left:198px;top:47px">Who We Are</h2>
  <div class="text">
    <p>Ut wisi enim ad minim veniam, quis nostrud exerci tation ullamcorper nibh euismod tincidunt ut laoreet dolore magna aliquam erat volutpat. Ut wisi enim ad minim veniam, quis nostrud exerci, tincidunt ut laoreet dolore magna aliquam erat volutpat. Ut wisi enim ad minim veniam, quis nostrud exerci, tincidunt ut laoreet dolore magna aliquam erat volutpat. Ut wisi enim ad minim veniam, quis.</p>
    <p>Ut wisi enim ad minim veniam, quis nostrud exerci tation ullamcorper nibh euismod tincidunt ut laoreet dolore magna aliquam erat volutpat. Ut wisi enim ad minim veniam.</p>
  </div>
  <div class="confidential light" style="right:15px;bottom:7px">Confidential and proprietary</div>
</section>

<section class="slide s3">
  <div class="lower"></div>
  <div class="abs" role="img" aria-label="Faint technical drawing of landing gear" style="left:6px;top:0;width:47px;height:87px;background:linear-gradient(180deg,rgba(180,186,196,.3),rgba(180,186,196,.08))"></div>
  <h2 class="slide-title">Meet The Team</h2>
  <div class="member" style="left:29px">
    <div class="portrait" role="img" aria-label="Portrait photo of the chief executive" style="background:linear-gradient(180deg,#3a3d42,#1c2230)"></div>
    <div class="name">Marek Olsen</div><div>CEO</div>
  </div>
  <div class="member" style="left:137px">
    <div class="portrait" role="img" aria-label="Portrait photo of the chief financial officer" style="background:linear-gradient(180deg,#7a7d80,#2b2d31)"></div>
    <div class="name">Tomas Delaine</div><div>CFO</div>
  </div>
  <div class="member" style="left:244px">
    <div class="portrait" role="img" aria-label="Portrait photo of the chief operating officer" style="background:linear-gradient(180deg,#e9edf2,#c9d2dc)"></div>
    <div class="name">Jonah Pryce</div><div>COO</div>
  </div>
  <div class="confidential" style="right:15px;bottom:7px">Confidential and proprietary</div>
</section>

<section class="slide s4">
  <div class="side"></div>
  <h2 class="slide-title">What We Do</h2>
  <div class="lead">Vestibulum nisl ipsum, aliquet sed viverra ut</div>
  <p class="body">malesuada ultrices hendrerit. Cras sagittis dui vitae purus ultricies, at egestas erat auctor. Sed auctor velit porta condimentum volutpat. In eget lacus eros. In ac luctus justo. Etiam felis diam, sodales eu dui in, pretium molestie orci. Etiam facilisis mollis lectus, non tempor dolor dictum sit amet.</p>
  <ul>
    <li>Etiam pretium mi vitae orci ipsum primis in faucibus porttitor.</li>
    <li>Efficitur magna rhoncus.</li>
    <li>Vestibulum ante ipsum primis in faucibus orci luctus et ultrices posuere</li>
    <li>Cubilia curae; Interdum et malesuada fames ac ante.</li>
  </ul>
  <div class="photo" role="img" aria-label="Photo of pilots in a cockpit" style="left:193px;top:74px;width:78px;height:54px;background:linear-gradient(160deg,#c9b79a,#3a3a38 70%)"></div>
  <div class="photo" role="img" aria-label="Photo of a small aircraft cockpit over the sea" style="left:283px;top:36px;width:60px;height:92px;background:linear-gradient(180deg,#a9c7de,#4a5660 70%)"></div>
  <div class="photo" role="img" aria-label="Photo of a jet on the apron at sunset" style="left:193px;top:134px;width:150px;height:104px;background:linear-gradient(180deg,#5e4a2e 0%,#e3b34a 40%,#8a7a62 60%,#6c655c 100%)"></div>
  <div class="confidential" style="right:15px;bottom:7px">Confidential and proprietary</div>
</section>

<section class="slide s5">
  <h2 class="slide-title">Who We Serve</h2>
  <div class="client" style="left:67px;top:87px"><span class="badge navy">A</span><h3>Insert Client Name Here</h3><p>Nam vitae pharetra libero. Vivamus faucibus sapien leo, luctus ultricies turpis.</p></div>
  <div class="client" style="left:67px;top:138px"><span class="badge navy">B</span><h3>Insert Client Name Here</h3><p>Nam vitae pharetra libero. Vivamus faucibus sapien leo, luctus ultricies turpis.</p></div>
  <div class="client" style="left:67px;top:188px"><span class="badge navy">C</span><h3>Insert Client Name Here</h3><p>Nam vitae pharetra libero. Vivamus faucibus sapien leo, luctus ultricies turpis.</p></div>
  <div class="client" style="left:225px;top:87px"><span class="badge cyan">D</span><h3 class="dark">Insert Client Name Here</h3><p>Nam vitae pharetra libero. Vivamus faucibus sapien leo, luctus ultricies turpis.</p></div>
  <div class="client" style="left:225px;top:138px"><span class="badge cyan">E</span><h3 class="dark">Insert Client Name Here</h3><p>Nam vitae pharetra libero. Vivamus faucibus sapien leo, luctus ultricies turpis.</p></div>
  <div class="client" style="left:225px;top:188px"><span class="badge cyan">F</span><h3 class="dark">Insert Client Name Here</h3><p>Nam vitae pharetra libero. Vivamus faucibus sapien leo, luctus ultricies turpis.</p></div>
  <div class="footer-band"></div>
  <div class="confidential" style="right:15px;bottom:7px">Confidential and proprietary</div>
</section>

<section class="slide s6">
  <div class="photo" role="img" aria-label="Photo of an aircraft cabin with a passenger by a sunlit window" style="left:0;top:0;width:360px;height:110px;background:linear-gradient(90deg,#4a3a3c 0%,#7a6a58 45%,#e6d9a8 78%,#5a4038 100%)"></div>
  <div class="step" style="left:29px"><div class="num light">01</div><span class="line"></span><h4>Insert title here</h4><p>Maecenas vitae urna tristique, rutrum ante at, porttitor risus. Nullam vitae augue eleifend, finibus urna at, ultrices sapien. Curabitur vulputate rhoncus turpis, sit amet gravida mauris.</p></div>
  <div class="step" style="left:112px"><div class="num">02</div><span class="line"></span><h4>Insert title here</h4><p>Aenean malesuada efficitur nibh, eget ultricies arcu euismod eu. Nam rutrum tristique justo, a mattis ante. Nunc vel lobortis justo, ornare pulvinar turpis. Duis condimentum est ac sapien sollicitudin, faucibus auctor augue semper.</p></div>
  <div class="step" style="left:196px"><div class="num">03</div><span class="line"></span><h4>Insert title here</h4><p>Praesent cursus ornare odio vitae mattis. Integer bibendum nisi id accumsan laoreet. Proin vel viverra augue, ut scelerisque massa. Morbi sed hendrerit ipsum. Orci varius natoque penatibus et magnis dis parturient montes, nascetur ridiculus mus.</p></div>
  <div class="step" style="left:279px"><div class="num" style="color:var(--navy)">04</div><h4>Insert title here</h4><p>Nullam ut mi facilisis, bibendum elit a, gravida turpis. Integer viverra ex id erat iaculis eleifend. Phasellus hendrerit blandit varius. Maecenas sagittis nulla neque, ac viverra felis auctor amet.</p></div>
  <div class="footer-band"></div>
  <div class="confidential" style="right:15px;bottom:7px">Confidential and proprietary</div>
</section>

</body>
</html>
```